Vendor Managed Inventory Talking points/Customer hand out

Looking for a single page flyer/Customer handout to be a sell sheet for our Vendor managed Inventory programs
Title: VMI benefits
Risk management:
Identification of Items and values that are sole sourced
Ongoing plans to reduce exposure to sole sourced items
Schedule planning to eliminate freight and outages
Reducing the hidden costs of forecasting errors
(Note; with us managing the point of use we can more accurately forecast)
Managing ever shortening of product lifecycles, minimizing obsolescence
Zero Inventory Exposure:
Minimized or Zero inventory on commodity items
Greatly reducing the Weighted Cost of Capital (WACC)
Reduced WACC can help in calculating Hurdle Rates
True point of use billing:
Allows for better tracking and allocation of expenses from a job-job basis
Custom labeling:
Including things like customer part numbers, exp dates, internal hazmat codes
Insures accurate processes with current materials
Helps to meet 5S requirements
Required for certain audits
Lot tracking/Shelf life:
Active assistance in managing Date Codes/Lot Tracking
Shortened shelf life products identified and managed
Plain statement of expiration dates on products. Calculations are not required
Taken as a whole we can help calculate TRUE management and landed costs of products. Focusing only on the price of items is like looking at just the exposed part of an iceberg. Let RT7K help you to see what's underneath.
I have attached some other brochures and flyers for style reference
more info on our website too. www.rt7k-example.com
Target Market(s)
Electronics manufacturers
Industry/Entity Type
Electronics
Look and feel

```html
<!DOCTYPE html>
<html lang="en">
<head>
<meta charset="utf-8">
<title>VMI Benefits – RT7K Sell Sheet</title>
<link rel="stylesheet" href="https://fonts.googleapis.com/css2?family=Oswald:wght@400;500;600&family=Open+Sans:wght@400;700&display=swap">
<style>
  :root {
    --stage: #bdbdbd;
    --blue: #1c4f96;
    --navy: #0f2f63;
    --ink: #333a44;
    --paper: #ffffff;
    --paper-shade: #e4e6ea;
    --photo-dark: #2a2c30;
    --photo-light: #9aa0a6;
  }
  * { margin: 0; padding: 0; box-sizing: border-box; }
  html, body { width: 801px; height: 1200px; overflow: hidden; }
  body { background: var(--stage); position: relative; font-family: "Open Sans", Arial, sans-serif; }

  .flyer {
    position: absolute; left: 40px; top: 134px;
    width: 720px; height: 931px;
    background: linear-gradient(180deg, var(--paper) 40%, var(--paper-shade) 100%);
    overflow: hidden;
    box-shadow: 0 2px 8px rgba(0,0,0,.25);
  }
  .flyer__photo {
    position: absolute; left: 0; top: 0; width: 720px; height: 380px;
    background: linear-gradient(90deg, var(--photo-dark) 0%, var(--photo-light) 45%, #6f757c 60%, #c9cdd1 100%);
  }
  .flyer__swoosh { position: absolute; left: 0; top: 320px; width: 720px; height: 90px; }

  .flyer__title {
    position: absolute; left: 106px; top: 362px; width: 512px; height: 86px;
    background: var(--blue);
    color: #fff; text-align: center;
    font-family: "Oswald", "Arial Narrow", sans-serif; font-weight: 500;
    font-size: 64px; line-height: 86px; letter-spacing: 1px;
  }

  .benefit { position: absolute; width: 330px; }
  .benefit__heading {
    font-family: "Oswald", "Arial Narrow", sans-serif; font-weight: 400;
    font-size: 19px; line-height: 22px; color: var(--blue);
    padding-left: 18px; position: relative; text-transform: uppercase;
  }
  .benefit__heading::before {
    content: ""; position: absolute; left: 0; top: 6px;
    width: 10px; height: 10px; border-radius: 50%; background: var(--ink);
  }
  .benefit__list { list-style: none; padding-left: 18px; margin-top: 2px; }
  .benefit__list li { font-size: 11.6px; line-height: 16.5px; color: var(--ink); }

  .benefit--risk { left: 17px; top: 478px; }
  .benefit--labeling { left: 17px; top: 645px; }
  .benefit--zero { left: 374px; top: 478px; }
  .benefit--billing { left: 374px; top: 585px; }
  .benefit--lot { left: 374px; top: 661px; }

  .flyer__summary {
    position: absolute; left: 35px; top: 768px; width: 660px;
    font-size: 11.6px; line-height: 16.5px; color: var(--ink);
  }

  .flyer__footer { position: absolute; left: 0; top: 800px; width: 720px; height: 131px; }
  .flyer__footer svg { position: absolute; left: 0; top: 0; }
  .contact {
    position: absolute; left: 38px; top: 30px;
    color: #fff; font-weight: 700; font-size: 31px; line-height: 44px;
  }
  .brand {
    position: absolute; right: 48px; top: 46px;
    display: flex; align-items: center; gap: 10px;
    color: #fff; font-weight: 700; font-size: 40px; line-height: 1;
  }
  .brand__dot { width: 16px; height: 16px; border-radius: 50%; background: #fff; }
</style>
</head>
<body>
  <article class="flyer">
    <div class="flyer__photo" role="img" aria-label="Photo of stockroom shelving with rows of clear plastic parts bins and component drawers"></div>
    <svg class="flyer__swoosh" viewBox="0 0 720 90" preserveAspectRatio="none" aria-hidden="true">
      <path d="M0 30 Q360 -10 720 40 L720 90 L0 90 Z" fill="var(--navy)"/>
      <path d="M0 42 Q360 5 720 52 L720 90 L0 90 Z" fill="var(--blue)"/>
      <path d="M0 52 Q360 18 720 62 L720 90 L0 90 Z" fill="#ffffff"/>
    </svg>

    <h1 class="flyer__title">VMI BENEFITS</h1>

    <section class="benefit benefit--risk">
      <h2 class="benefit__heading">Risk Management:</h2>
      <ul class="benefit__list">
        <li>Identification of Items and values that are sole sourced</li>
        <li>Ongoing plans to reduce exposure to sole sourced items</li>
        <li>Schedule planning to eliminate freight and outages</li>
        <li>Reducing the hidden costs of forecasting errors</li>
        <li>(Note: with us managing the point of use we can more accurately forecast)</li>
        <li>Managing ever shortening of product lifecycles, minimizing obsolescence</li>
      </ul>
    </section>

    <section class="benefit benefit--labeling">
      <h2 class="benefit__heading">Custom Labeling:</h2>
      <ul class="benefit__list">
        <li>Including things like customer part numbers, exp dates, internal hazmat codes</li>
        <li>Insures accurate processes with current materials</li>
        <li>Helps to meet 5S requirements</li>
        <li>Required for certain audits</li>
      </ul>
    </section>

    <section class="benefit benefit--zero">
      <h2 class="benefit__heading">Zero Inventory Exposure:</h2>
      <ul class="benefit__list">
        <li>Minimized or Zero inventory on commodity items</li>
        <li>Greatly reducing the Weighted Cost of Capital (WACC)</li>
        <li>Reduced WACC can help in calculating Hurdle Rates</li>
      </ul>
    </section>

    <section class="benefit benefit--billing">
      <h2 class="benefit__heading">True Point of Use Billing:</h2>
      <ul class="benefit__list">
        <li>Allows for better tracking and allocation of expenses from a job-job basis</li>
      </ul>
    </section>

    <section class="benefit benefit--lot">
      <h2 class="benefit__heading">Lot Tracking/Shelf Life:</h2>
      <ul class="benefit__list">
        <li>Active assistance in managing Date Codes/Lot Tracking Shortened shelf life products identified and managed Plain statement of expiration dates on products. Calculations are not required</li>
      </ul>
    </section>

    <p class="flyer__summary">Taken as a whole we can help calculate TRUE management and landed costs of products. Focusing only on the price of items is like looking at just the exposed part of an iceberg. Let RT7K help you to see what's underneath.</p>

    <footer class="flyer__footer">
      <svg width="720" height="131" viewBox="0 0 720 131" aria-hidden="true">
        <path d="M0 14 Q360 0 720 14 L720 131 L0 131 Z" fill="var(--navy)"/>
        <path d="M0 20 Q360 6 720 20 L720 131 L0 131 Z" fill="var(--blue)"/>
      </svg>
      <div class="contact">
        <div class="contact__web">www.rt7k-example.com</div>
        <div class="contact__phone">800.555.0142</div>
      </div>
      <div class="brand"><span class="brand__dot"></span><span class="brand__name">RT7K</span></div>
    </footer>
  </article>
</body>
</html>
```